Email Signature Design

Please design an email signature, the below is an example of our current design;
___

CARRODY ESTATE HOLDINGS PTY LTD
BENEDICT HARLOWE
Licensed Strata and Community Manager

143 Tallowood Street,
KELDARRA NSW 2093

P: 02.9473.6820 F: 9536.2048
Website: www.carrodyestate.com.au

This e-mail message and accompanying data may contain information that is confidential and private. If you are not the intended recipient, the use, dissemination, distribution or copying of this message or data is prohibited.

If you have received this e-mail in error please notify us immediately and delete all material pertaining to this e-mail. strata@carrodyestate.com.au

___

We would like to incorporate our logo and company colours, you can view the colours and feel of image at www.carrodyestate.com.au

Industry/Entity Type

It Company

Requirements
Must have
• use of logo and company colours (image)

```html
<!DOCTYPE html>
<html lang="en">
<head>
<meta charset="utf-8">
<title>Carrody Estate Holdings – Email Signature</title>
<link rel="stylesheet" href="https://fonts.googleapis.com/css2?family=Libre+Franklin:wght@400;500;600;700&display=swap">
<style>
  :root {
    --paper: #fcfbf7;
    --olive: #7b7d31;
    --ink: #5a5a5a;
    --ink-dark: #555555;
    --faint: #d9d7c4;
  }
  html, body {
    margin: 0;
    padding: 0;
    overflow: hidden;
    background: var(--paper);
  }
  .signature {
    position: relative;
    width: 927px;
    height: 1200px;
    background: var(--paper);
    font-family: "Libre Franklin", Arial, sans-serif;
    color: var(--ink);
    overflow: hidden;
  }
  .brand {
    position: absolute;
    left: 85px;
    top: 88px;
  }
  .brand-square {
    display: block;
    width: 150px;
    height: 150px;
    background: var(--olive);
  }
  .brand-name {
    margin: 22px 0 0;
    font-size: 33px;
    font-weight: 700;
    letter-spacing: 0.5px;
    line-height: 1;
    color: var(--olive);
  }
  .divider {
    position: absolute;
    left: 56px;
    top: 366px;
    width: 820px;
    height: 3px;
    background: var(--olive);
  }
  .contact {
    position: absolute;
    left: 91px;
    top: 442px;
    margin: 0;
    font-style: normal;
  }
  .contact p { margin: 0; }
  .company {
    font-size: 22px;
    font-weight: 600;
    line-height: 30px;
    color: var(--ink-dark);
  }
  .person {
    font-size: 25px;
    font-weight: 700;
    line-height: 34px;
    color: var(--olive);
    letter-spacing: 0.3px;
  }
  .role, .address, .phones, .web {
    font-size: 23px;
    line-height: 34px;
    color: var(--ink);
  }
  .address, .phones { margin-top: 32px !important; }
  .web { color: var(--olive); }
  .disclaimer {
    position: absolute;
    left: 82px;
    top: 822px;
    width: 800px;
    font-size: 18.5px;
    line-height: 26.7px;
    color: var(--ink-dark);
  }
  .disclaimer p { margin: 0 0 27px; }
  .disclaimer .email { color: var(--olive); font-weight: 700; }
  .footer-mark {
    position: absolute;
    left: 0;
    width: 927px;
    top: 1080px;
    text-align: center;
    font-size: 26px;
    font-weight: 700;
    letter-spacing: 0.5px;
    color: var(--faint);
  }
  .footer-band {
    position: absolute;
    left: 0;
    bottom: 0;
    width: 927px;
    height: 21px;
    background: var(--olive);
  }
</style>
</head>
<body>
  <div class="signature">
    <header class="brand">
      <span class="brand-square"></span>
      <p class="brand-name">CARRODY ESTATE</p>
    </header>

    <div class="divider"></div>

    <address class="contact">
      <p class="company">CARRODY ESTATE HOLDINGS PTY LTD</p>
      <p class="person">BENEDICT HARLOWE</p>
      <p class="role">Licensed Strata and Community Manager</p>
      <p class="address">143 Tallowood Street,<br>KELDARRA NSW 2093</p>
      <p class="phones">P: 02.9473.6820 F: 9536.2048</p>
      <p class="web">Website: www.carrodyestate.com.au</p>
    </address>

    <section class="disclaimer">
      <p>This email message and accompanying data may contain information that is confidential and private. If you are not the intended recipinet, the use, dissemination, distribution or copying of this message or data is probited.</p>
      <p>If you have received this e-mail in error please notify us immediately and delete all material pertaining to this email: <span class="email">strata@carrodyestate.com.au</span></p>
    </section>

    <div class="footer-mark">CARRODY ESTATE</div>
    <div class="footer-band"></div>
  </div>
</body>
</html>
```